SipNOW Business Cards

Hi designers!

Here's some background on our start-up and this project:

SipNOW is a website that will allow users to order alcohol from nearby liquor stores and have it delivered to their homes in minutes. We are really excited to work on creating the best online, alcohol purchasing experience for the users.

So why SipNOW? We like to think of ourselves as that great friend who will get alcohol for you because he happens to have a car. We help you drink in with your friends, family, or guests. Our site will target students and young professionals (of drinking age) who are comfortable buying things online or through apps. We don't see this service as a luxury, VIP, or niche service in the least; instead, we think of us as a relaxed, service-driven start-up that believes in simple design and transparent .

Now, we want a business card that incorporates our newly acquired logo design and some complimenting colors and fonts. Feel free to do it single or double sided, although I'm a sucker for double...

If you happen to have any questions, want to throw some ideas around, or just want some feedback- email me at marco@sipnow.example.

Marco Tessin
Founder

Industry/Entity Type

Business

Requirements
Must have
• Name, Position, Email, Cell-phone

No address, no fax, no land-line.

```html
<!DOCTYPE html>
<html lang="en">
<head>
<meta charset="utf-8">
<title>SipNOW Business Cards</title>
<link rel="stylesheet" href="https://fonts.googleapis.com/css2?family=Montserrat:wght@400;700;800;900&display=swap">
<style>
  :root {
    --backdrop: #1f1f1f;
    --paper: #f4f4f4;
    --ink: #1c1c1c;
    --muted: #5a5a5a;
    --sun: #f5be1e;
  }
  * { margin: 0; padding: 0; box-sizing: border-box; }
  html, body {
    width: 1200px;
    height: 901px;
    overflow: hidden;
    background: var(--backdrop);
    font-family: "Montserrat", sans-serif;
  }
  .stage {
    position: relative;
    width: 1200px;
    height: 901px;
  }
  .card {
    position: absolute;
    width: 520px;
    height: 297px;
    overflow: hidden;
    box-shadow: 0 18px 40px rgba(0,0,0,.55);
  }
  /* Front side */
  .card-front {
    left: 60px;
    top: 160px;
    background: var(--paper);
    color: var(--ink);
  }
  .holder {
    position: absolute;
    left: 40px;
    top: 56px;
  }
  .holder-name {
    font-weight: 700;
    font-size: 13px;
    color: var(--muted);
  }
  .holder-role {
    font-weight: 400;
    font-size: 12px;
    color: var(--muted);
    margin-top: 1px;
  }
  .front-wordmark {
    position: absolute;
    right: 40px;
    top: 122px;
    font-weight: 900;
    font-size: 38px;
    letter-spacing: -1px;
    color: var(--ink);
  }
  .contacts {
    position: absolute;
    left: 40px;
    bottom: 40px;
    display: grid;
    grid-template-columns: auto auto;
    column-gap: 12px;
    row-gap: 1px;
    font-size: 12.5px;
    line-height: 1.25;
  }
  .contact-label {
    font-weight: 700;
    color: var(--sun);
  }
  .contact-value {
    font-weight: 400;
    color: var(--muted);
  }
  /* Back side */
  .card-back {
    left: 620px;
    top: 444px;
    background: var(--sun);
  }
  .back-wordmark {
    position: absolute;
    left: 6px;
    bottom: -24px;
    font-weight: 900;
    font-size: 128px;
    letter-spacing: -5px;
    line-height: 1;
    color: var(--ink);
    white-space: nowrap;
  }
</style>
</head>
<body>
<main class="stage">
  <section class="card card-front" aria-label="Business card front">
    <div class="holder">
      <p class="holder-name">Marco Tessin</p>
      <p class="holder-role">Founder</p>
    </div>
    <p class="front-wordmark">SipNOW</p>
    <div class="contacts">
      <span class="contact-label">cell</span><span class="contact-value">5550 100 200</span>
      <span class="contact-label">email</span><span class="contact-value">marco@sipnow.example</span>
      <span class="contact-label">web</span><span class="contact-value">www.sipnow.example</span>
    </div>
  </section>
  <section class="card card-back" aria-label="Business card back">
    <p class="back-wordmark">SipNOW</p>
  </section>
</main>
</body>
</html>
```